Print on top the name of the company: (Or Similar)
Bellhaven Cleaning & Disinfecting
Because your standards aren't standard.

We adhere to ALL FHB guidelines for both residential and commercial cleaning.

Infection Control is our ultimate goal.

Instructions:
Opening a residential and commercial cleaning and disinfecting company in south Florida.

Targeting high-end residential clients, commercial and healthcare facilities, specializing in Ambulatory Care Guidelines. With a concentration and expertise in targeting Covid 19 and other transmissible pathogens.

TWLR trained.
Owned and operated by a licensed BSN Registered Nurse specially ​trained in Infection Control Prevention with over 25 years experience. Over two decades in Ambulatory Surgery Center Administration, Director of Nursing and Infection Control Prevention ad Consulting.

Looking to create a business flier that emphasizes Cleaning & Disinfection
along with the standard expectation for residential and Commercial cleaning services

Target Market(s)

Residential & Commercial

Font styles to use
Decorative

Requirements
Must have
• A checklist for cleaning services

```html
<!DOCTYPE html>
<html lang="en">
<head>
<meta charset="utf-8">
<title>Bellhaven Cleaning &amp; Disinfecting – Flyer</title>
<link rel="stylesheet" href="https://fonts.googleapis.com/css2?family=Anton&family=Poppins:wght@400;500;600;700;800;900&display=swap">
<style>
  :root{
    --green:#9cc42d;
    --yellow:#ffec00;
    --ink:#3d3d3d;
    --pill-dark:#505050;
    --white:#ffffff;
    --body:#555555;
    --stage:#4b4343;
  }
  *{margin:0;padding:0;box-sizing:border-box}
  html,body{width:1200px;height:2371px;overflow:hidden;background:var(--stage)}
  .stage{position:absolute;left:0;top:410px;width:1200px;height:1550px;overflow:hidden}
  .flyer{position:absolute;left:0;top:0;width:1056px;height:1364px;transform:scale(1.13636);transform-origin:0 0;overflow:hidden;background:var(--white);font-family:"Poppins",sans-serif;color:var(--ink)}
  .backdrop{position:absolute;left:0;top:0;width:1056px;height:1364px}
  .abs{position:absolute;white-space:nowrap}
  .mid{transform:translateY(-50%)}

  .center-col{left:580px;width:480px;text-align:center}
  .brand-name{top:61px;font-family:"Anton",sans-serif;font-size:58px;line-height:1;color:var(--white);letter-spacing:.5px}
  .brand-sub{top:106px;font-size:22px;line-height:1;color:var(--white)}

  .headline{font-weight:800;line-height:1;letter-spacing:-.5px}
  .hl-1{top:166px;font-size:36px;color:var(--ink)}
  .hl-2{top:214px;font-size:58px;color:var(--ink)}
  .hl-3{top:272px;font-size:58px;color:var(--green)}
  .hl-4{top:330px;font-size:58px;color:var(--yellow)}

  .tagline{right:37px;top:431px;text-align:right;color:var(--white);font-weight:700;font-size:22px;line-height:26px}

  .goal{right:37px;text-align:right;font-weight:800;font-size:29px;line-height:1;letter-spacing:-.3px}
  .goal-1{top:607px;color:var(--green)}
  .goal-2{top:640px;color:var(--ink)}
  .about{right:37px;top:669px;text-align:right;font-size:16.5px;line-height:24.7px;color:var(--body)}
  .about b{color:var(--ink);font-weight:700}

  .pill{left:667px;width:300px;height:42px;border-radius:21px;background:var(--green);color:var(--white);font-weight:700;font-size:25px;line-height:42px;text-align:center;padding-right:40px}
  .pill-res{top:799px}
  .pill-com{top:949px}
  .badge-icon{left:940px;width:72px;height:72px;border-radius:50%;background:var(--yellow);border:4px solid var(--white);box-shadow:0 0 0 2px var(--yellow);display:flex;align-items:center;justify-content:center}
  .icon-res{top:784px}
  .icon-com{top:934px}
  .badge-icon svg{width:40px;height:40px}

  .checklist{list-style:none;font-size:16.5px;line-height:25px;color:var(--body)}
  .checklist li{position:relative;padding-left:16px}
  .checklist li::before{content:"";position:absolute;left:0;top:8px;width:10px;height:10px;border-radius:50%;background:var(--green)}
  .checklist li::after{content:"";position:absolute;left:3.5px;top:10px;width:3px;height:5px;border:solid var(--white);border-width:0 1.5px 1.5px 0;transform:rotate(45deg)}
  .res-list{top:867px}
  .com-list{top:1013px}

  .seal{left:36px;top:514px;width:310px;height:310px;border-radius:50%;background:var(--yellow);border:8px solid var(--white)}
  .seal-line{position:absolute;left:0;width:100%;text-align:center;line-height:1}
  .seal-1{top:44px;font-size:64px;font-weight:900;color:var(--white);letter-spacing:1px}
  .seal-2{top:116px;font-size:31px;font-weight:500;color:var(--ink)}
  .seal-rule{position:absolute;left:26px;right:26px;top:154px;height:2px;background:var(--white)}
  .seal-3{top:168px;font-size:47px;font-weight:900;color:var(--white)}
  .seal-4{top:221px;font-size:31px;font-weight:500;color:var(--ink)}

  .window-photo{left:654px;top:1072px;width:402px;height:292px;background:radial-gradient(ellipse at 60% 55%,#d4d8dd 0%,#e8ebee 45%,rgba(255,255,255,0) 75%)}

  .cta-col{left:167px;width:432px;text-align:center}
  .cta{top:1154px;color:var(--green);font-weight:800;font-size:21.5px;line-height:28px}
  .phone{left:167px;top:1232px;width:432px;height:58px;border-radius:29px;background:var(--pill-dark);display:flex;align-items:center;padding-left:32px;gap:14px;color:var(--white);font-weight:600;font-size:38px;line-height:1}
  .phone-icon{width:42px;height:42px;border-radius:50%;background:var(--green);display:flex;align-items:center;justify-content:center;border:3px solid var(--white);flex:none}
  .web{top:1316px;font-size:19px;color:var(--ink)}
  .web strong{color:var(--green);font-weight:700}
</style>
</head>
<body>
<div class="stage">
<div class="flyer">
  <svg class="backdrop" viewBox="0 0 1056 1364">
    <defs>
      <linearGradient id="crewTone" x1="0" y1="0" x2="1" y2="1">
        <stop offset="0" stop-color="#eceef0"/>
        <stop offset=".55" stop-color="#d3d8dc"/>
        <stop offset="1" stop-color="#7fa3a6"/>
      </linearGradient>
    </defs>
    <rect width="1056" height="1364" fill="var(--green)"/>
    <rect x="570" y="136" width="486" height="230" fill="var(--white)"/>
    <path d="M0,0 H512 C592,180 592,420 482,590 C445,645 395,668 340,675 L0,695 Z" fill="var(--yellow)"/>
    <g role="img" aria-label="Photo of a technician in protective suit, mask and gloves spraying disinfectant">
      <path d="M0,0 H472 C548,170 550,400 452,560 C420,605 380,630 340,640 L0,662 Z" fill="url(#crewTone)"/>
    </g>
    <path d="M1056,498 C700,515 330,600 225,890 C150,1090 92,1250 80,1364 H1056 Z" fill="var(--yellow)"/>
    <path d="M1056,584 C700,565 360,645 255,905 C175,1100 118,1250 104,1364 H1056 Z" fill="var(--white)"/>
  </svg>

  <div class="abs center-col brand-name mid">BELLHAVEN</div>
  <div class="abs center-col brand-sub mid">CLEANING &amp; DISINFECTING</div>

  <div class="abs center-col headline hl-1 mid">BECAUSE YOUR</div>
  <div class="abs center-col headline hl-2 mid">STANDARDS</div>
  <div class="abs center-col headline hl-3 mid">AREN'T</div>
  <div class="abs center-col headline hl-4 mid">STANDARD</div>

  <div class="abs tagline mid">We Adhere To All FHB Guidelines For<br>Residential And Commercial Cleaning</div>

  <div class="abs goal goal-1 mid">INFECTION CONTROL</div>
  <div class="abs goal goal-2 mid">IS OUR ULTIMATE GOAL</div>
  <p class="abs about">Owned and operated by a licensed <b>BSN</b> Registered Nurse specially<br>trained in Infection Control Prevention with over <b>25 years experience</b>.<br>Over two decades in Ambulatory Surgery Center Administration, Director<br>of Nursing and Infection Control Prevention ad Consulting.</p>

  <div class="abs pill pill-res">RESIDENTIAL</div>
  <div class="abs badge-icon icon-res">
    <svg viewBox="0 0 48 48" fill="none" stroke="#fff" stroke-width="3" stroke-linejoin="round"><path d="M6 18 L10 8 H38 L42 18 Z"/><path d="M6 18 Q12 24 18 18 Q24 24 30 18 Q36 24 42 18"/><path d="M9 22 V41 H39 V22"/><path d="M20 41 V30 H28 V41"/></svg>
  </div>
  <ul class="abs checklist res-list" style="left:218px"><li>Janitorial</li><li>Offices</li></ul>
  <ul class="abs checklist res-list" style="left:374px"><li>Floor maintenance</li><li>Carpet cleaning</li></ul>
  <ul class="abs checklist res-list" style="left:615px"><li>Move-ins</li><li>Move-outs</li></ul>
  <ul class="abs checklist res-list" style="left:786px"><li>constructions clean-ups</li><li>Estate clean-outs</li></ul>

  <div class="abs pill pill-com">COMMERCIAL</div>
  <div class="abs badge-icon icon-com">
    <svg viewBox="0 0 48 48" fill="none" stroke="#fff" stroke-width="3" stroke-linejoin="round"><path d="M5 24 L24 7 L43 24"/><path d="M11 19 V41 H37 V19"/><path d="M20 41 V29 H28 V41"/></svg>
  </div>
  <ul class="abs checklist com-list" style="left:158px"><li>House cleaning</li><li>Before and after party</li></ul>
  <ul class="abs checklist com-list" style="left:405px"><li>Move-ins</li><li>Move-outs</li></ul>
  <ul class="abs checklist com-list" style="left:555px"><li>Holiday cleaning</li><li>Seasonal cleaning</li></ul>
  <ul class="abs checklist com-list" style="left:770px"><li>Carpet cleaning</li><li>Deodorizing and sanitizing</li></ul>

  <div class="abs seal">
    <div class="seal-line seal-1">TWLR</div>
    <div class="seal-line seal-2">TRAINED</div>
    <div class="seal-rule"></div>
    <div class="seal-line seal-3">25 YEARS</div>
    <div class="seal-line seal-4">EXPERIENCE</div>
  </div>

  <div class="abs window-photo" role="img" aria-label="Photo of a cleaner in gloves washing a bright window with a squeegee"></div>

  <p class="abs cta-col cta">CALL US TO FIND OUT HOW YOU CAN<br>SAVE MONEY THIS MONTH!</p>
  <div class="abs phone">
    <span class="phone-icon"><svg width="22" height="22" viewBox="0 0 24 24" fill="#fff"><path d="M6.6 10.8a15.1 15.1 0 0 0 6.6 6.6l2.2-2.2a1 1 0 0 1 1-.25 11.4 11.4 0 0 0 3.6.57 1 1 0 0 1 1 1V20a1 1 0 0 1-1 1A17 17 0 0 1 3 4a1 1 0 0 1 1-1h3.5a1 1 0 0 1 1 1c0 1.25.2 2.45.57 3.6a1 1 0 0 1-.25 1z"/></svg></span>
    <span>(305) 555 01 82</span>
  </div>
  <p class="abs cta-col web mid">www.<strong>BellhavenCleaning&amp;Disinfecting</strong>.com</p>
</div>
</div>
</body>
</html>
```